4 page brochure for Logistics Company

Need a 4 page brochure (ie folded A3) for a Logistics company.
Service is a virtual network of warehouse and logistics companies.
Style is professional but accessible.
We have logo and styles designed and will upload these.
We have identified example images that could be used in the brochure.
Content will be uploaded also.
Updates
Reason: A couple of designers requested more time
Am giving another 24 hours to finalise and will then select most suitable design
Target Market(s)
40 to 60 year old business owners (traditional) - Australian
Industry/Entity Type
It Company
Requirements
Must have
- Professional
Should not have
- Nothing tacky

```html
<!DOCTYPE html>
<html lang="en">
<head>
<meta charset="utf-8">
<title>Meridian Logistics Network – Brochure Spread</title>
<link rel="stylesheet" href="https://fonts.googleapis.com/css2?family=Open+Sans:ital,wght@0,400;0,600;0,700;1,400&family=Titillium+Web:wght@300;400&display=swap">
<style>
  :root{
    --brand-blue:#1b74b8;
    --brand-blue-deep:#0f4f8a;
    --sky:#2aa0dc;
    --slate:#6d8596;
    --panel-grey:#ececec;
    --ink:#4a4a4a;
    --paper:#ffffff;
    --backdrop:#2b2b2b;
  }
  *{margin:0;padding:0;box-sizing:border-box}
  html,body{width:1200px;height:960px;overflow:hidden;background:var(--backdrop);font-family:"Open Sans",sans-serif;color:var(--ink)}
  .spread{position:absolute;left:10px;top:62px;width:1251px;height:885px;background:var(--paper);transform:scale(0.9433);transform-origin:0 0;overflow:hidden}
  .spread-art{position:absolute;left:0;top:0}
  .abs{position:absolute}
  .title-light{font-family:"Titillium Web",sans-serif;font-weight:300;color:#fff;font-size:31px;line-height:1}
  .intro-italic{font-style:italic;font-size:10.8px;line-height:17px}
  .section-heading{font-family:"Titillium Web",sans-serif;font-weight:300;color:var(--brand-blue);font-size:17.5px;line-height:26px}
  .tick-list{list-style:none}
  .tick-list li{position:relative;padding-left:16px;font-size:10px;line-height:13px}
  .tick{position:absolute;left:0;top:1px;width:11px;height:11px}
  .dynamics li{position:absolute;width:272px}
  .exit-row{position:absolute;left:0;width:625px;background:var(--panel-grey)}
  .exit-tag{position:absolute;left:0;top:0;width:232px;height:48px;color:#fff;font-size:11px;line-height:17px}
  .exit-tag svg{position:absolute;left:0;top:0}
  .exit-tag-text{position:relative;display:block;padding:8px 0 0 18px;width:200px}
  .exit-tag b{font-weight:700}
  .exit-tag i{font-style:italic}
  .exit-row .tick-list{position:absolute;left:242px;width:350px}
  .exit-row .tick-list li{margin-bottom:13px}
  .solution-title{font-family:"Titillium Web",sans-serif;color:var(--brand-blue);font-weight:300;font-size:31px;line-height:42px}
  .benefit{position:absolute;left:672px;width:561px;background:var(--slate);color:#fff}
  .benefit .tick-list{position:absolute;left:45px;right:8px}
  .benefit .tick-list li{margin-bottom:13px;font-size:9.6px;line-height:13px}
  .benefit .tick-list li:last-child{margin-bottom:0}
  .badge{position:absolute;left:640px;width:62px;height:62px;border-radius:50%;background:var(--brand-blue);border:3px solid #fff;color:#fff;font-size:12px;line-height:15px;display:flex;align-items:center;justify-content:center;text-align:center}
  .chart-label{font-size:6px;fill:#666;font-family:"Open Sans",sans-serif}
</style>
</head>
<body>
<svg width="0" height="0" style="position:absolute">
  <defs>
    <symbol id="tick" viewBox="0 0 12 12">
      <circle cx="6" cy="6" r="5" fill="none" stroke="currentColor" stroke-width="1.3"/>
      <path d="M3.4 6.2 5.3 8 9 4" fill="none" stroke="currentColor" stroke-width="1.4"/>
    </symbol>
  </defs>
</svg>

<main class="spread">
  <svg class="spread-art" width="1251" height="885" viewBox="0 0 1251 885">
    <defs>
      <linearGradient id="bandBlue" x1="0" y1="0" x2="1" y2="0">
        <stop offset="0" stop-color="#0f5a9c"/>
        <stop offset=".6" stop-color="#1e8fd0"/>
        <stop offset="1" stop-color="#1a6fb4"/>
      </linearGradient>
      <radialGradient id="photoTone" cx=".78" cy=".42" r=".7">
        <stop offset="0" stop-color="#3c7fd0"/>
        <stop offset=".5" stop-color="#1a4c9c"/>
        <stop offset="1" stop-color="#0b2a5e"/>
      </radialGradient>
    </defs>
    <path d="M0 0H830C700 80 450 150 0 162Z" fill="url(#bandBlue)"/>
    <path d="M345 145C480 128 600 112 692 102L668 68C560 108 450 134 345 145Z" fill="#6f8290"/>
    <path role="img" aria-label="Photo of hanging light bulbs, one glowing brightly" d="M835 0H1251V360C1050 372 845 285 665 68C730 40 790 20 835 0Z" fill="url(#photoTone)"/>
  </svg>

  <!-- Page 1 -->
  <h1 class="abs title-light" style="left:20px;top:32px">The challenges (Why?)</h1>
  <p class="abs intro-italic" style="left:22px;top:76px;width:410px;color:#fff">Australian warehouse business owners are facing unprecedented challenges to diversify their client base, compete for work with national clients, enhance their profitability and ultimately, exit their business.</p>

  <h2 class="abs section-heading" style="left:20px;top:186px">AUSTRALIAN WAREHOUSE INDUSTRY DYNAMICS</h2>
  <ul class="tick-list dynamics" style="position:absolute;left:20px;top:0;color:var(--brand-blue)">
    <li style="top:225px"><svg class="tick"><use href="#tick"/></svg><span style="color:var(--ink)">Exceptionally fragmented - 1,600 businesses across Australia</span></li>
    <li style="top:264px"><svg class="tick"><use href="#tick"/></svg><span style="color:var(--ink)">Single site operators – increasing challenge to compete against corporates to secure larger contracts</span></li>
    <li style="top:316px"><svg class="tick"><use href="#tick"/></svg><span style="color:var(--ink)">Accelerating industry consolidation</span></li>
    <li style="top:342px"><svg class="tick"><use href="#tick"/></svg><span style="color:var(--ink)">Substantial margin pressure – Gross Profits falling 3% FY13 to FY15</span></li>
    <li style="top:381px"><svg class="tick"><use href="#tick"/></svg><span style="color:var(--ink)">High customer concentration risk</span></li>
    <li style="top:407px"><svg class="tick"><use href="#tick"/></svg><span style="color:var(--ink)">Ongoing need to invest in technology to maintain market share</span></li>
  </ul>

  <svg class="abs" style="left:340px;top:255px" width="260" height="160" viewBox="0 0 260 160" role="img" aria-label="Gross profit area chart, falling from 42.5% in FY13 to 39% in FY15">
    <g stroke="#e2e2e2" stroke-width=".6">
      <line x1="32" y1="12" x2="250" y2="12"/><line x1="32" y1="24" x2="250" y2="24"/><line x1="32" y1="36" x2="250" y2="36"/><line x1="32" y1="48" x2="250" y2="48"/><line x1="32" y1="60" x2="250" y2="60"/><line x1="32" y1="72" x2="250" y2="72"/><line x1="32" y1="84" x2="250" y2="84"/><line x1="32" y1="96" x2="250" y2="96"/><line x1="32" y1="108" x2="250" y2="108"/><line x1="32" y1="120" x2="250" y2="120"/><line x1="32" y1="132" x2="250" y2="132"/>
    </g>
    <line x1="32" y1="0" x2="32" y2="132" stroke="#bbb" stroke-width=".6"/>
    <polygon points="53,18 230,97 230,132 53,132" fill="#3f9ac8"/>
    <g class="chart-label" text-anchor="end">
      <text x="28" y="14">43.00%</text><text x="28" y="26">42.50%</text><text x="28" y="38">42.00%</text><text x="28" y="50">41.50%</text><text x="28" y="62">41.00%</text><text x="28" y="74">40.50%</text><text x="28" y="86">40.00%</text><text x="28" y="98">39.50%</text><text x="28" y="110">39.00%</text><text x="28" y="122">38.50%</text><text x="28" y="134">38.00%</text>
    </g>
    <g class="chart-label" text-anchor="middle"><text x="53" y="147">FY13</text><text x="142" y="147">FY14</text><text x="227" y="147">FY15</text></g>
    <text x="105" y="24" font-size="11" fill="#333" font-family="Open Sans, sans-serif">Gross Profit (approx)</text>
  </svg>

  <h2 class="abs section-heading" style="left:18px;top:485px">WAREHOUSE OWNERS HAVE A CHALLENGE TO EXIT THEIR BUSINESS</h2>

  <section class="exit-row" style="top:532px;height:48px">
    <div class="exit-tag"><svg width="232" height="48"><path d="M0 0H215L232 24 215 48H0Z" fill="#1b74b8"/></svg><span class="exit-tag-text"><b>Glut of sellers</b> <i>Many warehouse owners are aging</i></span></div>
    <ul class="tick-list" style="top:8px;color:var(--brand-blue)">
      <li style="line-height:17px"><svg class="tick"><use href="#tick"/></svg><span style="color:var(--ink)">The first “baby boomer” owners turn 69 in 2015 and are within reach of retirement</span></li>
    </ul>
  </section>

  <section class="exit-row" style="top:588px;height:154px">
    <div class="exit-tag" style="height:50px"><svg width="232" height="50"><path d="M0 0H215L232 25 215 50H0Z" fill="#1b74b8"/></svg><span class="exit-tag-text"><b>Inability to attract buyers</b><br><i>Owners have limited ability to sell</i></span></div>
    <ul class="tick-list" style="top:13px;color:var(--brand-blue)">
      <li><svg class="tick"><use href="#tick"/></svg><span style="color:var(--ink)">Many single-site operators lack the size and scale to attract a corporate buyer</span></li>
      <li><svg class="tick"><use href="#tick"/></svg><span style="color:var(--ink)">Succession through the family is often not an option e.g. no interest from next generation to take on the business risk</span></li>
      <li><svg class="tick"><use href="#tick"/></svg><span style="color:var(--ink)">Many businesses difficult to sell due to dependence on owner operator</span></li>
      <li><svg class="tick"><use href="#tick"/></svg><span style="color:var(--ink)">Low EBIT would not attract financial buyers</span></li>
    </ul>
  </section>

  <section class="exit-row" style="top:755px;height:90px">
    <div class="exit-tag"><svg width="232" height="48"><path d="M0 0H215L232 24 215 48H0Z" fill="#1b74b8"/></svg><span class="exit-tag-text"><b>Need to cash-out</b> <i>Yet many owners have genuine need to sell</i></span></div>
    <ul class="tick-list" style="top:12px;color:var(--brand-blue)">
      <li><svg class="tick"><use href="#tick"/></svg><span style="color:var(--ink)">Substantial capital costs that need to be recovered</span></li>
      <li><svg class="tick"><use href="#tick"/></svg><span style="color:var(--ink)">Long-term leases with substantial penalties for early termination</span></li>
      <li><svg class="tick"><use href="#tick"/></svg><span style="color:var(--ink)">Need to fund retirement</span></li>
    </ul>
  </section>

  <!-- Page 2 -->
  <h1 class="abs solution-title" style="left:641px;top:220px">The solution<br>(What?)</h1>
  <p class="abs intro-italic" style="left:645px;top:319px;width:325px">Meridian Logistics Network provides a national platform to deliver scale its members. Through this scale, MLN and its members will secure new business. The value of members’ businesses will increase, and members will be presented with multiple options to exit.</p>
  <h2 class="abs section-heading" style="left:644px;top:426px;width:535px">MLN PROVIDES DELIVERS SCALE, SYNERGIES, VALUE &amp; POTENTIAL EXIT TO ITS MEMBERSHIP</h2>

  <section class="benefit" style="top:491px;height:95px">
    <ul class="tick-list" style="top:8px">
      <li><svg class="tick"><use href="#tick"/></svg>By leveraging its membership and national presence, MLN will present as a premium logistics provider within the Australian market – a credible alternative to the large corporates</li>
      <li><svg class="tick"><use href="#tick"/></svg>Initial scale at launch is intended to exceed 100,000m2 with over $50 million in annual turnover</li>
      <li><svg class="tick"><use href="#tick"/></svg>MLN provides its members with a national network</li>
    </ul>
  </section>
  <div class="badge" style="top:509px">Scale</div>

  <section class="benefit" style="top:592px;height:73px">
    <ul class="tick-list" style="top:16px">
      <li><svg class="tick"><use href="#tick"/></svg>MLN will provide a centralised business development function on behalf of its members</li>
      <li><svg class="tick"><use href="#tick"/></svg>Where MLN can leverage its scale, it will provide reduce costs to its members</li>
    </ul>
  </section>
  <div class="badge" style="top:599px">Synergy</div>

  <section class="benefit" style="top:672px;height:81px">
    <ul class="tick-list" style="top:16px">
      <li><svg class="tick"><use href="#tick"/></svg>Members’ businesses will increase in value as new work is introduced &amp; customer base is diversified</li>
      <li><svg class="tick"><use href="#tick"/></svg>With its scale, the ultimate sale of MLN will be at a higher multiple and value than any individual member could achieve</li>
    </ul>
  </section>
  <div class="badge" style="top:684px">Value</div>

  <section class="benefit" style="top:760px;height:82px">
    <ul class="tick-list" style="top:16px">
      <li><svg class="tick"><use href="#tick"/></svg>For members who wish to sell some or all of their business,<br>MLN will offer to acquire part of their business</li>
      <li><svg class="tick"><use href="#tick"/></svg>This initial exit will enable owners to “take some cash off the table” and de-risk</li>
    </ul>
  </section>
  <div class="badge" style="top:769px">Potential<br>Exit</div>
</main>
</body>
</html>
```